Assessment Flyer

We are looking for a marketing flyer for our business. We are a psychology practice that has recently expanded our assessment team and availability. We need a flyer to fax to GP's and other referrers. We have previously sent out rather basic flyers as it was more of a courtesy update about our practice rather than a marketing tool. We have recently created a brochure just focusing on assessments which can be used as a guide for the flyer. We want to update them about our expansion, highlight the assessments we do, introduce our new psychologists, and touch on availability.

```html
<!DOCTYPE html>
<html lang="en">
<head>
<meta charset="utf-8">
<title>Assessment Services Flyer</title>
<link href="https://fonts.googleapis.com/css2?family=Montserrat:wght@400;500;600;700;800;900&display=swap" rel="stylesheet">
<style>
:root{
  --teal:#13a89e;
  --teal-dark:#0f7f77;
  --name:#13706a;
  --green:#7cc242;
  --green-text:#6ab43a;
  --stage:#eceef0;
  --white:#ffffff;
  --rule:#e2e6e6;
  --scrub:#9fcde6;
  --scrub-deep:#86c1df;
  --coat:#f6f8f9;
  --clinic:#e4ebee;
}
*{margin:0;padding:0;box-sizing:border-box}
html,body{width:1200px;height:2210px;overflow:hidden;background:var(--stage);font-family:"Montserrat",sans-serif}
.canvas{position:relative;width:1200px;height:2210px}
.flyer{position:absolute;left:50px;top:393px;width:875px;height:1132px;background:var(--white);
  transform:scale(1.2571);transform-origin:0 0;box-shadow:0 20px 50px rgba(0,0,0,.18);overflow:hidden}
.abs{position:absolute}

.header{left:0;top:0;width:875px;height:520px;background:linear-gradient(#fff 0,#f4f6f7 100px,#e8edef 300px)}
.team-photo{left:0;top:80px;width:875px;height:440px;
  background:
    linear-gradient(180deg,#fbfcfc 0,rgba(251,252,252,0) 22%),
    radial-gradient(ellipse 11% 38% at 13% 66%,var(--coat) 0,rgba(246,248,249,0) 100%),
    radial-gradient(ellipse 13% 46% at 31% 64%,var(--scrub) 0,rgba(159,205,230,0) 100%),
    radial-gradient(ellipse 12% 44% at 48% 70%,var(--scrub-deep) 0,rgba(134,193,223,0) 100%),
    radial-gradient(ellipse 11% 44% at 64% 64%,var(--coat) 0,rgba(246,248,249,0) 100%),
    radial-gradient(ellipse 10% 40% at 80% 70%,var(--scrub) 0,rgba(159,205,230,0) 100%),
    radial-gradient(ellipse 10% 48% at 94% 62%,var(--scrub-deep) 0,rgba(134,193,223,0) 100%),
    linear-gradient(180deg,var(--clinic) 0,#d9e5ea 55%,#cfe1ea 100%)}
.header-fade{left:0;top:360px;width:875px;height:160px;background:linear-gradient(rgba(19,168,158,0),rgba(19,168,158,.8) 50%,var(--teal))}
.brand{left:0;top:38px;width:875px;text-align:center;font-weight:600;font-size:34px;color:var(--teal);letter-spacing:.5px}
.brand-dot{display:inline-block;width:26px;height:26px;border-radius:50%;background:var(--green);vertical-align:-3px;margin-right:12px}
.title-box{left:128px;top:378px;width:614px;height:59px;background:var(--green);border:3px solid #fff;
  color:#fff;font-weight:900;font-size:43px;text-align:center;line-height:53px;letter-spacing:.5px}
.intro{left:40px;top:453px;width:795px;text-align:center;color:#fff;font-size:14.5px;line-height:17.5px;font-weight:500}
.intro b{font-weight:700}

.team-heading{left:0;top:540px;width:875px;text-align:center;color:var(--green);font-weight:900;font-size:24px;letter-spacing:.3px}
.rule{height:1px;background:var(--rule)}
.tree-art{left:285px;top:590px;width:305px;height:275px;border-radius:48% 48% 12% 12%;
  background:radial-gradient(ellipse at 50% 40%,#d4ecca 0,#e6f4e0 55%,rgba(255,255,255,0) 75%)}
.member{width:260px}
.member .name{color:var(--name);font-weight:700;font-size:17px;line-height:19px}
.member .role{color:var(--green-text);font-weight:400;font-size:14px;line-height:17px}
.left{text-align:right}

.assess-bar{left:56px;top:900px;width:762px;height:95px;border-radius:12px;background:linear-gradient(var(--green) 0,#5cbb5c 60%,#2fb08a 100%)}
.assess-pill{left:244px;top:870px;width:389px;height:55px;border-radius:14px;background:var(--teal);border:3px solid #fff;
  color:#fff;font-weight:600;font-size:24px;text-align:center;line-height:49px;letter-spacing:.3px}
.assess-item{top:948px;display:flex;align-items:center;gap:8px;color:#fff;font-size:12px;line-height:13px;font-weight:500}
.assess-item svg{width:28px;height:28px;flex:none}

.availability{left:0;top:1008px;width:875px;text-align:center;font-size:16px;color:var(--green-text)}
.availability .label{font-weight:600;text-decoration:underline;margin-right:8px}

.footer{left:0;top:1045px;width:875px;height:87px;background:var(--teal)}
.f-item{display:flex;align-items:center;gap:9px;color:#fff;font-size:12px;line-height:14px}
.f-item svg{width:18px;height:18px;flex:none}
.f-line{font-size:15px}
.f-phone{font-size:17px;font-weight:700}
</style>
</head>
<body>
<div class="canvas">
  <div class="flyer">
    <div class="abs header"></div>
    <div class="abs team-photo" role="img" aria-label="Photo of six smiling clinicians in white lab coats and light blue scrubs standing with arms crossed in a bright clinic corridor"></div>
    <div class="abs header-fade"></div>
    <div class="abs brand"><span class="brand-dot"></span>Harbourside Psychology &amp; Wellness</div>

    <div class="abs title-box">ASSESSMENT SERVICES</div>
    <p class="abs intro">Harbourside Psychology and Wellness is excited to announce the expansion of our assessment team.<br><b>As the need for assessment services has grown, we have worked diligently to expand our team<br>with highly skilled psychologists to support these needs.</b></p>

    <h2 class="abs team-heading">MEET THE ASSESSMENT TEAM</h2>

    <div class="abs rule" style="left:225px;top:624px;width:200px"></div>
    <div class="abs rule" style="left:225px;top:684px;width:200px"></div>
    <div class="abs rule" style="left:225px;top:743px;width:200px"></div>
    <div class="abs rule" style="left:225px;top:802px;width:200px"></div>
    <div class="abs rule" style="left:450px;top:624px;width:190px"></div>
    <div class="abs rule" style="left:450px;top:684px;width:190px"></div>
    <div class="abs rule" style="left:450px;top:743px;width:190px"></div>
    <div class="abs rule" style="left:450px;top:802px;width:190px"></div>
    <div class="abs tree-art" role="img" aria-label="Soft green illustrated tree with leaves"></div>

    <div class="abs member left" style="left:-47px;top:609px"><div class="name">Dr Maren Castell</div><div class="role">Clinical Director</div></div>
    <div class="abs member left" style="left:-47px;top:669px"><div class="name">Dr Ruth Calder</div><div class="role">Registered Psychologist</div></div>
    <div class="abs member left" style="left:-47px;top:728px"><div class="name">Dr Ilsa Hartmann</div><div class="role">Counselling Psychologist</div></div>
    <div class="abs member left" style="left:-47px;top:787px"><div class="name">Nadia Fiorentino</div><div class="role">Registered Psychologist</div></div>

    <div class="abs member" style="left:653px;top:609px"><div class="name">Carina Valentini</div><div class="role">Registered Psychologist</div></div>
    <div class="abs member" style="left:653px;top:669px"><div class="name">Tessa Marlow</div><div class="role">Provisional Psychologist</div></div>
    <div class="abs member" style="left:653px;top:728px"><div class="name">Lucy Brennan</div><div class="role">Provisional Psychologist</div></div>
    <div class="abs member" style="left:654px;top:787px"><div class="name">Gabriela Ortega<br>Whitfield</div><div class="role">Registered Psychologist</div></div>

    <div class="abs assess-bar"></div>
    <div class="abs assess-pill">AVAILABLE ASSESSMENTS</div>

    <div class="abs assess-item" style="left:82px">
      <svg viewBox="0 0 28 28" fill="#fff"><circle cx="14" cy="6" r="4"/><path d="M4 14l10 4 10-4v10l-10 3-10-3z"/></svg>
      <span>Educational<br>Assessment</span>
    </div>
    <div class="abs assess-item" style="left:220px">
      <svg viewBox="0 0 28 28" fill="none" stroke="#fff" stroke-width="2.2"><path d="M8 25v-5c-3-2-4-5-4-8a10 10 0 0 1 20 0l2 5h-3v4h-5v4"/><circle cx="14" cy="12" r="3"/></svg>
      <span>ADHD: Children<br>and Adults</span>
    </div>
    <div class="abs assess-item" style="left:382px">
      <svg viewBox="0 0 28 28" fill="#fff"><path d="M4 8h6a3 3 0 1 1 6 0h6v6a3 3 0 1 0 0 6v5h-6a3 3 0 1 0-6 0H4v-6a3 3 0 1 1 0-6z"/></svg>
      <span>Autism: Children<br>and Adults</span>
    </div>
    <div class="abs assess-item" style="left:555px">
      <svg viewBox="0 0 28 28" fill="#fff"><circle cx="9" cy="9" r="4"/><path d="M2 26v-6a7 7 0 0 1 14 0v6z"/><rect x="17" y="2" width="9" height="10" rx="1" fill="none" stroke="#fff" stroke-width="2"/></svg>
      <span>Intellectual<br>Disability</span>
    </div>
    <div class="abs assess-item" style="left:692px">
      <svg viewBox="0 0 28 28" fill="#fff"><path d="M14 1l3.6 7.6 8.4 1-6.2 5.8 1.6 8.4L14 19.6 6.6 23.8l1.6-8.4L2 9.6l8.4-1z"/></svg>
      <span>Giftedness</span>
    </div>

    <p class="abs availability"><span class="label">AVAILABILITY</span>Appointments available from early March 2024.</p>

    <div class="abs footer"></div>
    <div class="abs f-item" style="left:20px;top:1062px">
      <svg viewBox="0 0 18 18" fill="#fff"><path d="M9 1a6 6 0 0 0-6 6c0 4.5 6 10 6 10s6-5.5 6-10a6 6 0 0 0-6-6zm0 8.5A2.5 2.5 0 1 1 9 4.5a2.5 2.5 0 0 1 0 5z"/></svg>
      <span>41 Coastal Parade<br>Seacliff Vale, SA 5099</span>
    </div>
    <div class="abs f-item" style="left:224px;top:1062px">
      <svg viewBox="0 0 18 18" fill="#fff"><path d="M9 1a6 6 0 0 0-6 6c0 4.5 6 10 6 10s6-5.5 6-10a6 6 0 0 0-6-6zm0 8.5A2.5 2.5 0 1 1 9 4.5a2.5 2.5 0 0 1 0 5z"/></svg>
      <span>3/18 Marina Street<br>Seacliff Vale, SA 5099</span>
    </div>
    <div class="abs f-item f-line" style="left:24px;top:1100px">
      <svg viewBox="0 0 18 18" fill="none" stroke="#fff" stroke-width="1.8"><rect x="2" y="4" width="14" height="10" rx="1"/><path d="M2 5l7 5 7-5"/></svg>
      <span>reception@harbourpsychwellness.com.au</span>
    </div>
    <div class="abs f-item f-phone" style="left:523px;top:1067px">
      <svg viewBox="0 0 18 18" fill="#fff"><path d="M4 1.5l3 .5 1 4-2 1.5a10 10 0 0 0 4.5 4.5L12 10l4 1 .5 3-2 2.5C8 16 2 10 1.5 3.5z"/></svg>
      <span>08 7100 2384</span>
    </div>
    <div class="abs f-item f-phone" style="left:696px;top:1067px">
      <svg viewBox="0 0 18 18" fill="#fff"><rect x="1" y="6" width="4" height="11"/><path d="M6 3h8v4h3v10H6zm2 6v2h2V9zm4 0v2h2V9zm-4 4v2h2v-2zm4 0v2h2v-2z"/></svg>
      <span>08 6100 3719</span>
    </div>
    <div class="abs f-item f-line" style="left:523px;top:1099px">
      <svg viewBox="0 0 18 18" fill="none" stroke="#fff" stroke-width="1.5"><circle cx="9" cy="9" r="7.5"/><path d="M1.5 9h15M9 1.5c-4 4.5-4 10.5 0 15M9 1.5c4 4.5 4 10.5 0 15"/></svg>
      <span>www.harbourpsychwellness.com.au</span>
    </div>
  </div>
</div>
</body>
</html>
```